Showroom Quote Web Application - Material Design wanted

This web app is an internal application that will be used by one of our customers to build quotes and produce orders of retail items with their customers

the overall design should use the colour pallet provided and have a clean and simple interface

we'd like to go with a material design type of look

attached mockups are just a rough stab at some layouts to give you an example, please feel free to reach out with any questions.

Please don't get hung up on the specific pages, they were intended to provide context, we are looking for a high level design using the provided colour schemes and fonts, additional work may follow for the selected designer when it comes to specific pages or work flows.

Sorry for the short timeline, we have a tight deadline on this one.

Target Market(s)

internal application for customer

Industry/Entity Type

Retail

Other font styles liked:
• see attached doc for fonts

Requirements
Must have
• simple and clean interface
• intuitive design
Nice to have
• see attached documents for logo colour schemes and fonts
• these must be incorporated into the design

```html
<!DOCTYPE html>
<html lang="en">
<head>
<meta charset="utf-8">
<title>Harbor Showroom Quote System</title>
<link rel="stylesheet" href="https://fonts.googleapis.com/css2?family=Roboto:wght@400;500&family=Source+Sans+3:wght@400&display=swap">
<style>
  :root {
    --page-bg: #c5d5df;
    --gold: #a68a4a;
    --surface: #ffffff;
    --body-bg: #f1f1f1;
    --rule: #e2e2e2;
    --text: #222222;
    --muted: #7a7a7a;
    --faint: #b5b5b5;
    --link: #3d9ad8;
    --fab: #0d3a7a;
    --avatar: #8a7a72;
  }
  * { box-sizing: border-box; margin: 0; padding: 0; }
  html, body { width: 1200px; height: 674px; overflow: hidden; }
  body { background: var(--page-bg); font-family: "Roboto", sans-serif; position: relative; }

  .app { position: absolute; left: 118px; top: 60px; width: 964px; height: 548px;
         background: var(--body-bg); border-radius: 4px 4px 0 0; overflow: hidden;
         border-bottom: 4px solid var(--gold); }

  .app-bar { position: absolute; left: 0; top: 0; width: 100%; height: 57px; background: var(--gold); }
  .app-title { position: absolute; left: 51px; top: 16px; color: #fff;
               font-family: "Source Sans 3", sans-serif; font-size: 20px; }
  .user-name { position: absolute; right: 74px; top: 19px; color: #fff;
               font-family: "Source Sans 3", sans-serif; font-size: 14px; }
  .user-avatar { position: absolute; left: 896px; top: 8px; width: 40px; height: 40px;
                 border-radius: 50%; background: radial-gradient(circle at 50% 40%, #d9c2b4, var(--avatar)); }

  .toolbar { position: absolute; left: 0; top: 57px; width: 100%; height: 50px; background: var(--surface);
             box-shadow: 0 1px 2px rgba(0,0,0,.12); }
  .search { position: absolute; left: 92px; top: 14px; width: 180px; height: 23px;
            border-bottom: 1px solid var(--rule); color: var(--faint); font-size: 14px; }
  .search svg { position: absolute; left: 2px; top: 1px; }
  .search span { position: absolute; left: 22px; top: 1px; }
  .filter { position: absolute; left: 808px; top: 17px; color: var(--muted); font-size: 14px; }
  .filter svg { margin-left: 6px; vertical-align: middle; }

  .quote-table { position: absolute; left: 92px; top: 130px; width: 779px; height: 392px;
                 background: var(--surface); box-shadow: 0 1px 3px rgba(0,0,0,.15); }
  .row { position: relative; height: 47px; border-bottom: 1px solid var(--rule); font-size: 14.5px; color: var(--text); }
  .row.head { height: 57px; color: var(--muted); font-size: 15px; }
  .row.last { border-bottom: none; height: 52px; }
  .cell { position: absolute; top: 50%; transform: translateY(-50%); white-space: nowrap; }
  .sort { margin-left: 8px; vertical-align: middle; }
  .edit-link { color: var(--link); text-decoration: underline; }

  .fab { position: absolute; left: 1002px; top: 524px; width: 56px; height: 56px; border-radius: 50%;
         background: var(--fab); box-shadow: 0 3px 6px rgba(0,0,0,.25); }
  .fab svg { position: absolute; left: 18px; top: 18px; }
</style>
</head>
<body>
<div class="app">
  <header class="app-bar">
    <div class="app-title">Harbor Showroom Quote System</div>
    <div class="user-name">Laura Benett..</div>
    <div class="user-avatar" role="img" aria-label="User profile photo"></div>
  </header>

  <div class="toolbar">
    <div class="search">
      <svg width="16" height="16" viewBox="0 0 16 16"><circle cx="6.5" cy="6.5" r="5" fill="none" stroke="#b5b5b5" stroke-width="1.6"/><line x1="10" y1="10" x2="14.5" y2="14.5" stroke="#b5b5b5" stroke-width="1.8"/></svg>
      <span>Search</span>
    </div>
    <div class="filter">Filter<svg width="8" height="5" viewBox="0 0 8 5"><path d="M0 0h8L4 5z" fill="#b5b5b5"/></svg></div>
  </div>

  <section class="quote-table">
    <div class="row head">
      <div class="cell" style="left:36px">Quotes<svg class="sort" width="7" height="13" viewBox="0 0 7 13"><path d="M3.5 0L7 5H0z M3.5 13L0 8h7z" fill="#c2c2c2"/></svg></div>
      <div class="cell" style="left:198px">Customer<svg class="sort" width="7" height="13" viewBox="0 0 7 13"><path d="M3.5 0L7 5H0z M3.5 13L0 8h7z" fill="#c2c2c2"/></svg></div>
      <div class="cell" style="left:345px">Date<svg class="sort" width="7" height="13" viewBox="0 0 7 13"><path d="M3.5 0L7 5H0z M3.5 13L0 8h7z" fill="#c2c2c2"/></svg></div>
      <div class="cell" style="left:458px">Value<svg class="sort" width="7" height="13" viewBox="0 0 7 13"><path d="M3.5 0L7 5H0z M3.5 13L0 8h7z" fill="#c2c2c2"/></svg></div>
      <div class="cell" style="left:556px">Discription</div>
      <div class="cell" style="left:684px">View</div>
    </div>
    <div class="row">
      <div class="cell" style="left:36px">15554</div>
      <div class="cell" style="left:125px">Marco Bellavista</div>
      <div class="cell" style="left:300px">2017-09-30</div>
      <div class="cell" style="left:426px">$ 5,300.00</div>
      <div class="cell" style="left:552px">New House</div>
      <div class="cell" style="left:690px"><span class="edit-link">Edit</span></div>
    </div>
    <div class="row">
      <div class="cell" style="left:36px">15554</div>
      <div class="cell" style="left:125px">Marco Bellavista</div>
      <div class="cell" style="left:300px">2017-09-30</div>
      <div class="cell" style="left:426px">$ 5,300.00</div>
      <div class="cell" style="left:552px">New House</div>
      <div class="cell" style="left:690px"><span class="edit-link">Edit</span></div>
    </div>
    <div class="row">
      <div class="cell" style="left:36px">15554</div>
      <div class="cell" style="left:125px">Marco Bellavista</div>
      <div class="cell" style="left:300px">2017-09-30</div>
      <div class="cell" style="left:426px">$ 5,300.00</div>
      <div class="cell" style="left:552px">New House</div>
      <div class="cell" style="left:690px"><span class="edit-link">Edit</span></div>
    </div>
    <div class="row"></div>
    <div class="row"></div>
    <div class="row"></div>
    <div class="row last"></div>
  </section>

  <div class="fab" aria-label="New quote">
    <svg width="20" height="20" viewBox="0 0 20 20"><path d="M10 0v20M0 10h20" stroke="#fff" stroke-width="2.6"/></svg>
  </div>
</div>
</body>
</html>
```